Professional Services - letterhead / business cards

The company (veltaro holdings) will provide services to Investment Funds and large investors in Spain. I have recently chosen a logo that I am attaching.

I would like a simple stationary design that i could use as letter head, business cards and "with compliments" cards.

I am not quite sure which color I will mostly use for the logo, in the email signature I will probably lean towards the white background and grey letters. I am attaching my favourite options.

Target Market(s)

Large Multinationals, Investment funds and Law firms

Industry/Entity Type

Business

Requirements
Must have
• my details are:
Luis R. Andrade
Veltaro Holdings S.L.
Casa de Valdehondo
Calle del Olmo Tardío 42
28017 Madrid
T: +34 (91) 807-3356
M: +34 (655) 718-904
e-mail: landrade@veltaroholdings.example

```html
<!DOCTYPE html>
<html lang="en">
<head>
<meta charset="utf-8">
<title>Veltaro Holdings — Stationery</title>
<link rel="stylesheet" href="https://fonts.googleapis.com/css2?family=Questrial&family=Arimo:ital,wght@0,400;0,700;1,700&display=swap">
<style>
  :root {
    --brand-blue: #2323c4;
    --band-deep: #0b0b9c;
    --band-light: #2a2ad6;
    --ring: #dcdcf2;
    --rule-grey: #8a8a96;
    --rule-light: #c9c9d2;
    --paper: #ffffff;
    --canvas: #ffffff;
    --ink: #3a3a4a;
    --accent-pink: #d04cc8;
  }
  * { box-sizing: border-box; margin: 0; padding: 0; }
  html, body { width: 985px; height: 1200px; overflow: hidden; background: var(--canvas); }
  body { position: relative; font-family: "Arimo", Arial, sans-serif; color: var(--ink); }

  .sheet { position: absolute; background: var(--paper); overflow: hidden; box-shadow: 1px 2px 4px rgba(0,0,0,.35); }
  .sheet > svg.art { position: absolute; inset: 0; width: 100%; height: 100%; }
  .sheet > *:not(svg) { position: absolute; }

  .wordmark { font-family: "Questrial", sans-serif; color: var(--brand-blue); font-weight: 400; white-space: nowrap; letter-spacing: .5px; }

  /* Letterhead */
  .letterhead { left: 27px; top: 70px; width: 734px; height: 1038px; }
  .letterhead .holder-name { right: 44px; top: 44px; font-size: 14px; color: #dfe0ff; letter-spacing: 1px; }
  .letterhead .wordmark { left: 44px; top: 96px; font-size: 32px; }
  .letterhead .address { right: 42px; top: 110px; text-align: right; font-size: 10.5px; line-height: 13.5px; color: #333; }
  .address .company { font-weight: 700; color: var(--brand-blue); letter-spacing: .4px; }
  .letterhead .contacts { left: 0; right: 0; top: 954px; text-align: center; font-size: 11.5px; line-height: 15px; color: #555; }
  .contacts b { color: var(--brand-blue); }

  /* Business card */
  .business-card { left: 640px; top: 310px; width: 317px; height: 192px; }
  .business-card .wordmark { left: 16px; top: 16px; font-size: 18px; }
  .business-card .holder-name { left: 18px; top: 68px; font-size: 11px; font-weight: 700; color: #333; }
  .business-card .contacts { left: 16px; top: 152px; font-size: 6px; line-height: 8px; color: #e4e4ff; }
  .business-card .address { right: 14px; top: 136px; text-align: right; font-size: 6px; line-height: 8px; color: #e4e4ff; }
  .business-card .address .company { color: #c9b8ff; }

  /* Compliments card */
  .compliments-card { left: 439px; top: 560px; width: 518px; height: 366px; }
  .compliments-card .wordmark { left: 26px; top: 30px; font-size: 25px; }
  .compliments-card .greeting { right: 28px; top: 144px; font-size: 16px; font-weight: 700; font-style: italic; color: var(--brand-blue); letter-spacing: .5px; }
  .compliments-card .contacts { left: 26px; top: 308px; font-size: 9px; line-height: 12px; color: #e4e4ff; }
  .compliments-card .address { right: 24px; top: 284px; text-align: right; font-size: 9px; line-height: 12px; color: #e4e4ff; }
  .compliments-card .address .company { color: #c9b8ff; }
  .dark-contacts b { color: var(--accent-pink); }
</style>
</head>
<body>

<!-- Letterhead -->
<section class="sheet letterhead">
  <svg class="art" viewBox="0 0 734 1038" preserveAspectRatio="none" aria-hidden="true">
    <defs>
      <linearGradient id="lh-band" x1="0" x2="1" y1="0" y2="0">
        <stop offset="0" stop-color="var(--band-light)"/>
        <stop offset="1" stop-color="var(--band-deep)"/>
      </linearGradient>
      <linearGradient id="lh-rule" x1="0" x2="1">
        <stop offset="0" stop-color="var(--rule-light)"/>
        <stop offset=".5" stop-color="var(--rule-grey)"/>
        <stop offset="1" stop-color="var(--rule-grey)"/>
      </linearGradient>
    </defs>
    <circle cx="194" cy="816" r="200" fill="none" stroke="var(--ring)" stroke-width="44"/>
    <path d="M0 0 H734 V74 C600 82 500 36 320 44 C190 50 90 22 0 36 Z" fill="url(#lh-band)"/>
    <path d="M0 42 C90 28 190 56 320 50 C500 42 600 88 734 80" fill="none" stroke="#fff" stroke-width="4"/>
    <path d="M0 47 C90 34 190 62 320 56 C500 48 600 94 734 86" fill="none" stroke="#55555f" stroke-width="2"/>
    <rect x="0" y="183" width="734" height="4" fill="url(#lh-rule)"/>
    <rect x="0" y="191" width="734" height="2" fill="var(--rule-light)"/>
    <rect x="0" y="1012" width="734" height="3" fill="var(--rule-grey)"/>
    <rect x="0" y="1017" width="734" height="2" fill="var(--brand-blue)"/>
  </svg>
  <p class="holder-name">Luis R. Andrade</p>
  <p class="wordmark">veltaro holdings</p>
  <address class="address">
    <span class="company">VELTARO HOLDINGS S.L.</span><br>
    Casa de Valdehondo<br>
    Calle del Olmo Tardío 42<br>
    28017 Madrid
  </address>
  <p class="contacts">
    <b>T:</b> +34 (91) 807-3356<br>
    <b>M:</b> +34 (655) 718-904<br>
    <b>E:</b> landrade@veltaroholdings.example
  </p>
</section>

<!-- Business card -->
<section class="sheet business-card">
  <svg class="art" viewBox="0 0 317 192" preserveAspectRatio="none" aria-hidden="true">
    <defs>
      <linearGradient id="bc-band" x1="0" x2="1">
        <stop offset="0" stop-color="var(--band-deep)"/>
        <stop offset="1" stop-color="var(--band-light)"/>
      </linearGradient>
    </defs>
    <circle cx="250" cy="64" r="78" fill="none" stroke="var(--ring)" stroke-width="22"/>
    <circle cx="40" cy="240" r="70" fill="none" stroke="var(--ring)" stroke-width="20"/>
    <path d="M0 114 C90 122 180 82 317 92 V192 H0 Z" fill="url(#bc-band)"/>
    <path d="M0 108 C90 116 180 76 317 86" fill="none" stroke="#55555f" stroke-width="1.5"/>
    <path d="M0 111 C90 119 180 79 317 89" fill="none" stroke="#fff" stroke-width="2"/>
  </svg>
  <p class="wordmark">veltaro holdings</p>
  <p class="holder-name">Luis R. Andrade</p>
  <p class="contacts dark-contacts">
    <b>T:</b> +34 (91) 807-3356<br>
    <b>M:</b> +34 (655) 718-904<br>
    <b>E:</b> landrade@veltaroholdings.example
  </p>
  <address class="address">
    <span class="company">VELTARO HOLDINGS S.L.</span><br>
    Casa de Valdehondo<br>
    Calle del Olmo Tardío 42<br>
    28017 Madrid
  </address>
</section>

<!-- With compliments card -->
<section class="sheet compliments-card">
  <svg class="art" viewBox="0 0 518 366" preserveAspectRatio="none" aria-hidden="true">
    <defs>
      <linearGradient id="cc-band" x1="0" x2="1">
        <stop offset="0" stop-color="var(--band-deep)"/>
        <stop offset="1" stop-color="var(--band-light)"/>
      </linearGradient>
    </defs>
    <circle cx="404" cy="140" r="120" fill="none" stroke="var(--ring)" stroke-width="34"/>
    <circle cx="170" cy="420" r="110" fill="none" stroke="var(--ring)" stroke-width="34"/>
    <path d="M0 226 C120 250 260 180 518 200 V366 H0 Z" fill="url(#cc-band)"/>
    <path d="M0 218 C120 242 260 172 518 192" fill="none" stroke="#55555f" stroke-width="2"/>
    <path d="M0 222 C120 246 260 176 518 196" fill="none" stroke="#fff" stroke-width="3"/>
  </svg>
  <p class="wordmark">veltaro holdings</p>
  <p class="greeting">“With Compliments”</p>
  <p class="contacts dark-contacts">
    <b>T:</b> +34 (91) 807-3356<br>
    <b>M:</b> +34 (655) 718-904<br>
    <b>E:</b> landrade@veltaroholdings.example
  </p>
  <address class="address">
    <span class="company">VELTARO HOLDINGS S.L.</span><br>
    Casa de Valdehondo<br>
    Calle del Olmo<br>
    Tardío 42<br>
    28017 Madrid
  </address>
</section>

</body>
</html>
```